Personal Injury Funding Flyer

We are Qorva Financial, a provider of receivables management solutions to the surgical industry.
We want a 1 page flyer to showcase our Motor Vehicle Accident (MVA) and Personal Injury (PI) case management and lien purchasing.

1- a flyer from a competitor. We like the overall feel of the flyer and the simplicity of the information presented.

You can also check out our website for examples of our company's style
www.qorvafinancial-example.com

Target Market(s)

Surgeons, office managers, administrators and CFOS at smaller surgical facilities and surgical hospitals nationwide

Industry/Entity Type

Financial

Requirements
Must have
• Titled: Personal Injury Case Funding
• Tagline: We Ensure Your Cases are Financially Sound
• Include Qorva Financial's logo
• Be sure to boldly highlight the 3 points:
• 3 Steps to Successful PI Case Management
• 1) Evaluate Cases
• Evaluate the financial aspects of the case including policy limits.
• 2) Consult Attorneys
• Evaluate the case background and likelihood of settlement.
• 3) Guaranteed Funding
• 15 day funding on most cases.
• How Does MVA/PI Funding Work?
• We pay you upfront and wait for the case to settle.
• Our funding eliminates the risk, hassle and uncertainty associated with PI cases.
• You get paid 100% NON-RECOURSE
• Include contact phone number (800) 472-5190
• >No Hassles
• >No Risk
• >Guaranteed Funds.
Nice to have
• Smiling doctor picture
Should not have
• Too much information

```html
<!DOCTYPE html>
<html lang="en">
<head>
<meta charset="utf-8">
<title>Personal Injury Case Funding — Qorva Financial</title>
<link rel="stylesheet" href="https://fonts.googleapis.com/css2?family=Oswald:wght@400;500;600;700&family=Open+Sans:wght@400;600;700&display=swap">
<style>
  :root {
    --stage: #d9d3d3;
    --paper: #ebebeb;
    --maroon: #4b1515;
    --maroon-deep: #3c0f0f;
    --orange: #f0891b;
    --grey-text: #6b6b6b;
    --grey-badge: #6e6e70;
    --ink: #2c2c2c;
    --alert-red: #e3262a;
    --white: #ffffff;
  }
  * { box-sizing: border-box; margin: 0; padding: 0; }
  html, body { width: 1192px; height: 1200px; overflow: hidden; }
  body {
    background: var(--stage);
    font-family: "Open Sans", Arial, sans-serif;
    position: relative;
  }
  .flyer {
    position: absolute;
    left: 297px; top: 33px;
    width: 598px; height: 1134px;
    background: var(--paper);
    overflow: hidden;
  }
  .hero-photo {
    position: absolute; left: 0; top: 0;
    width: 598px; height: 494px;
    background: linear-gradient(110deg, #c9ccd0 0%, #e3e4e6 35%, #b9c4cf 60%, #dfe3e8 100%);
  }
  .title {
    position: absolute; left: 0; right: 0; top: 500px;
    text-align: center;
    font-family: "Oswald", "Arial Narrow", sans-serif;
    font-weight: 700; font-size: 46px; line-height: 1.1;
    color: var(--maroon);
    letter-spacing: -0.5px;
    white-space: nowrap;
  }
  .tagline {
    position: absolute; left: 0; right: 0; top: 558px;
    text-align: center;
    font-family: "Oswald", "Arial Narrow", sans-serif;
    font-weight: 400; font-size: 23px; line-height: 1.2;
    color: var(--grey-text);
    white-space: nowrap;
  }
  .steps-badge {
    position: absolute; left: 61px; top: 606px;
    width: 122px;
    text-align: center;
  }
  .steps-number {
    font-family: "Oswald", "Arial Narrow", sans-serif;
    font-weight: 700; font-size: 96px; line-height: 1;
    color: var(--maroon);
  }
  .steps-label {
    background: var(--maroon);
    color: var(--white);
    font-weight: 700; font-size: 15px; line-height: 1.3;
    padding: 7px 2px;
    white-space: nowrap;
  }
  .step-list { list-style: none; }
  .step-item { position: absolute; left: 196px; width: 250px; }
  .step-item.first { top: 626px; }
  .step-item.second { top: 694px; }
  .step-item.third { top: 762px; }
  .step-title {
    font-weight: 700; font-size: 18.5px; line-height: 1.2;
    color: var(--maroon);
    white-space: nowrap;
  }
  .step-text {
    margin-left: 44px;
    font-size: 13px; line-height: 1.3;
    color: var(--grey-text);
    white-space: nowrap;
  }
  .funding-tab {
    position: absolute; left: 454px; top: 604px;
    width: 144px; height: 144px;
    background: var(--orange);
    border-radius: 14px 0 0 14px;
    color: var(--white);
    text-align: center;
    font-family: "Oswald", "Arial Narrow", sans-serif;
    padding-top: 12px;
  }
  .funding-days { font-size: 60px; font-weight: 600; line-height: 1; }
  .funding-days small { font-size: 20px; font-weight: 500; }
  .funding-note { font-size: 20px; font-weight: 500; line-height: 1.15; }
  .promise-seal {
    position: absolute; left: 455px; top: 780px;
    width: 140px; height: 140px;
  }
  .promise-seal svg { width: 140px; height: 140px; }
  .promise-seal .seal-text {
    position: absolute; inset: 0;
    display: flex; flex-direction: column; justify-content: center; align-items: center;
    font-family: "Oswald", "Arial Narrow", sans-serif;
    font-weight: 500; font-size: 14.5px; line-height: 1.25;
    color: var(--white); text-align: center;
    transform: rotate(-15deg);
    white-space: nowrap;
  }
  .how-it-works {
    position: absolute; left: 61px; top: 830px; width: 390px;
    font-family: "Oswald", "Arial Narrow", sans-serif;
  }
  .how-title {
    font-weight: 600; font-size: 18px; line-height: 1.3; color: var(--maroon);
    margin-bottom: 2px;
  }
  .how-list {
    list-style: none; font-weight: 400; font-size: 14px; line-height: 1.65;
    color: var(--ink); white-space: nowrap;
  }
  .how-list li::before { content: "· "; }
  .non-recourse { color: var(--alert-red); }
  .brand {
    position: absolute; left: 61px; top: 936px;
    display: flex; align-items: center;
  }
  .brand-mark {
    width: 24px; height: 24px;
    background: var(--maroon-deep);
    margin-right: 10px;
  }
  .brand-name {
    font-family: "Oswald", "Arial Narrow", sans-serif;
    font-weight: 500; font-size: 30px; color: var(--grey-badge);
    line-height: 1;
  }
  .brand-divider {
    width: 1px; height: 48px; background: #b0b0b0;
    margin: 0 12px;
  }
  .brand-services {
    font-size: 12.5px; line-height: 1.35; color: var(--grey-text);
  }
  .contact-band {
    position: absolute; left: 0; bottom: 0;
    width: 598px; height: 112px;
    background: var(--maroon-deep);
    display: flex; align-items: center; justify-content: center;
    font-family: "Oswald", "Arial Narrow", sans-serif;
    font-weight: 600; font-size: 27px; color: var(--white);
    white-space: nowrap;
  }
  .contact-divider {
    width: 4px; height: 40px; background: var(--orange);
    margin: 0 12px;
  }
</style>
</head>
<body>
  <main class="flyer">
    <div class="hero-photo" role="img" aria-label="Photo of a smiling doctor in a white coat with a stethoscope, with a colleague attending a patient in a hospital bed behind him"></div>

    <h1 class="title">Personal Injury Case Funding</h1>
    <p class="tagline">We Ensure Your Cases are Financially Sound</p>

    <div class="steps-badge">
      <div class="steps-number">3</div>
      <div class="steps-label">Steps to<br>Successful<br>PI Case<br>Management</div>
    </div>

    <ol class="step-list">
      <li class="step-item first">
        <div class="step-title">1) Evaluate Cases</div>
        <div class="step-text">Evaluate the financial aspects of<br>the case including policy limits.</div>
      </li>
      <li class="step-item second">
        <div class="step-title">2) Consult Attorneys</div>
        <div class="step-text">Evaluate the case background<br>and likelihood of settlement.</div>
      </li>
      <li class="step-item third">
        <div class="step-title">3) Guaranteed Funding</div>
      </li>
    </ol>

    <div class="funding-tab">
      <div class="funding-days">15<small>day</small></div>
      <div class="funding-note">funding on<br>most cases.</div>
    </div>

    <div class="promise-seal">
      <svg viewBox="0 0 150 150" aria-hidden="true">
        <polygon fill="var(--grey-badge)" points="75,4 84,20 99,8 103,26 121,20 118,38 137,38 128,54 145,62 131,74 145,86 128,95 137,112 118,112 121,130 103,124 99,142 84,130 75,146 66,130 51,142 47,124 29,130 32,112 13,112 22,95 5,86 19,74 5,62 22,54 13,38 32,38 29,20 47,26 51,8 66,20"/>
      </svg>
      <div class="seal-text">No Hassles<br>No Risk<br>Guaranteed Funds</div>
    </div>

    <section class="how-it-works">
      <h2 class="how-title">How Does MVA/PI Funding Work?</h2>
      <ul class="how-list">
        <li>We pay you upfront and wait for the case to settle.</li>
        <li>Our funding eliminates the risk, hassle and uncertainty associated with PI cases.</li>
        <li>You get paid <span class="non-recourse">100% NON-RECOURSE</span></li>
      </ul>
    </section>

    <div class="brand">
      <span class="brand-mark"></span>
      <span class="brand-name">Qorva Financial</span>
      <span class="brand-divider"></span>
      <span class="brand-services">Receivable<br>Management<br>Solutions</span>
    </div>

    <footer class="contact-band">
      <span class="contact-web">www.qorvafinancial-example.com</span>
      <span class="contact-divider"></span>
      <span class="contact-phone">(800) 472-5190</span>
    </footer>
  </main>
</body>
</html>
```